Business Card for a Floral & Decorating Business

I would like to take my current logo and create a better business card. I am looking for elegance as I am a florist and event decorator. My logo has multiple colour options. I like colours like green, purple, pink and orange, I think I would like a white card, open to black back ground. I want it to feel elegant and romantic. I like metallic lettering that maybe is indented in the paper, I also like glossy paper. I have a full logo already as well as a badge. I have attached both in multiple colours.m
Updates

Need extra days to review

Target Market(s)

Weddings, special events, floral customers

Industry/Entity Type

Floral and decorating

Contact Information for Business Card

Phone number, email, instagram, facebook, title, name, logo

Font styles to use
Script

Requirements
Nice to have
• Elegant

```html
<!DOCTYPE html>
<html lang="en">
<head>
<meta charset="UTF-8">
<title>Marlow Hayes – Business Card</title>
<link rel="stylesheet" href="https://fonts.googleapis.com/css2?family=Great+Vibes&family=Playfair+Display:wght@700&family=Cormorant+Garamond:wght@500&family=Arimo:wght@400&display=swap">
<style>
  :root {
    --backdrop: #2b2b2b;
    --card: #7e6793;
    --card-accent: #a57db4;
    --ink: #ffffff;
  }
  * { box-sizing: border-box; margin: 0; padding: 0; }
  html, body { width: 1200px; height: 1015px; overflow: hidden; }
  body { background: var(--backdrop); position: relative; font-family: "Arimo", sans-serif; color: var(--ink); }

  .card {
    position: absolute;
    width: 640px;
    height: 366px;
    background: var(--card);
    box-shadow: 0 14px 30px rgba(0,0,0,.45);
    overflow: hidden;
  }
  .card--front { left: 140px; top: 90px; }
  .card--back  { left: 420px; top: 540px; }

  .brand {
    position: absolute;
    inset: 0;
    display: flex;
    flex-direction: column;
    align-items: center;
    justify-content: center;
    gap: 6px;
  }
  .brand__row { display: flex; align-items: center; gap: 16px; }
  .brand__mark {
    width: 36px; height: 36px;
    border: 2px solid var(--ink);
    border-radius: 50%;
  }
  .brand__name {
    font-family: "Great Vibes", cursive;
    font-size: 72px;
    font-weight: 400;
    line-height: 1;
  }
  .brand__tagline {
    font-family: "Cormorant Garamond", serif;
    font-weight: 500;
    font-size: 15px;
    letter-spacing: 0.42em;
    text-transform: uppercase;
    padding-left: 52px;
  }

  .contact { position: absolute; left: 48px; top: 104px; }
  .contact__name {
    font-family: "Playfair Display", serif;
    font-weight: 700;
    font-size: 30px;
    line-height: 1.1;
  }
  .contact__title { font-size: 18px; margin-top: 2px; }
  .contact__list { list-style: none; margin-top: 30px; }
  .contact__item {
    display: flex; align-items: center; gap: 10px;
    font-size: 19px; line-height: 1.4;
  }
  .contact__item svg { width: 18px; height: 18px; flex: none; }

  .social {
    position: absolute; left: 48px; bottom: 34px;
    display: flex; align-items: center; gap: 10px;
    font-size: 17px;
  }
  .social__dot { width: 26px; height: 26px; border-radius: 50%; background: var(--ink); }

  .emblem {
    position: absolute;
    right: 70px; top: 40px;
    width: 270px; height: 290px;
    border-radius: 50%;
    background: radial-gradient(circle at 50% 45%, var(--card-accent), var(--card) 72%);
    opacity: .55;
  }
</style>
</head>
<body>

  <section class="card card--front">
    <div class="brand">
      <div class="brand__row">
        <span class="brand__mark"></span>
        <span class="brand__name">Marlow Hayes</span>
      </div>
      <span class="brand__tagline">Decorating &amp; Florals.</span>
    </div>
  </section>

  <section class="card card--back">
    <div class="emblem" role="img" aria-label="Embossed floral monogram decoration"></div>

    <div class="contact">
      <h1 class="contact__name">Daniel Reeves</h1>
      <p class="contact__title">Managing Director</p>
      <ul class="contact__list">
        <li class="contact__item">
          <svg viewBox="0 0 24 24" fill="none" stroke="#fff" stroke-width="2"><path d="M5 3h4l2 5-2.5 1.5a11 11 0 0 0 6 6L16 13l5 2v4a2 2 0 0 1-2 2A16 16 0 0 1 3 5a2 2 0 0 1 2-2z"/></svg>
          044-987 654 321
        </li>
        <li class="contact__item">
          <svg viewBox="0 0 24 24" fill="none" stroke="#fff" stroke-width="2"><rect x="2" y="5" width="20" height="14"/><path d="M2 5l10 8 10-8"/></svg>
          hello@marlowhayes.com
        </li>
        <li class="contact__item">
          <svg viewBox="0 0 24 24" fill="none" stroke="#fff" stroke-width="2"><circle cx="12" cy="12" r="10"/><path d="M2 12h20M12 2a15 15 0 0 1 0 20M12 2a15 15 0 0 0 0 20"/></svg>
          www.marlowhayes.com
        </li>
      </ul>
    </div>

    <div class="social">
      <span class="social__dot"></span>
      <span class="social__handle">@marlowhayes</span>
    </div>
  </section>

</body>
</html>
```